Coffee House With Cycling Theme Wants Business Cards

We want to create a business card for a coffee house that has a cycling theme. We expect to use the current logo on one side of the business card and we have been considering adding the words 'COFFEE HOUSE' underneath (see example). For the other side of the business card we want an interesting design with tag-line, address and social media links (the normal business card stuff). See examples provided but we are not fixed on having it exactly as shown, we are very open to great creative ideas. Please note our logo has the initials ‘RM' in orange embedded in the design and this must be retained. However, you can play with the words COFFEE HOUSE as well as use the orange color on the backside of the business card, as you see fit. For an image on the backside of the business card it can be a photo, hand-drawn or whatever but it must visually combine coffee and cycling in some way. The interior of the Coffee House will be reclaimed wood, rustic and have an urban feel to it with cycling artifacts hanging from the walls/ceiling, etc. Finally, it would be beneficial if the business card design elements can be easily used on flyers and other promotional assets. Good luck, we are looking forward to seeing your creative ideas.

Target Market(s)

Coffee lovers and cycling fans

Contact Information for Business Card

See project description.

Colors

Designer to choose colors to be used in the design.

Requirements
Must have
• Must use the current logo provided and combine a coffee and bike theme.
Nice to have
• Orange is used in current logo and could be used as an accent color on the backside of the business card.

```html
<!DOCTYPE html>
<html lang="en">
<head>
<meta charset="utf-8">
<title>RM Coffee House – Business Card</title>
<link rel="stylesheet" href="https://fonts.googleapis.com/css2?family=Open+Sans:wght@300;400;600&display=swap">
<style>
  :root {
    --page: #ffffff;
    --card-light: #f6f5f3;
    --ink: #3d3d3d;
    --orange: #ff6a1f;
    --orange-soft: #ff7737;
    --bean: #a5471c;
    --white: #ffffff;
  }
  * { box-sizing: border-box; margin: 0; padding: 0; }
  html, body {
    width: 1084px; height: 1200px; overflow: hidden;
    background: var(--page);
    font-family: "Open Sans", sans-serif;
  }
  .card {
    position: absolute;
    left: 133px;
    width: 826px;
    height: 545px;
    box-shadow: 4px 5px 9px rgba(0,0,0,0.28);
  }

  /* Front */
  .card--front {
    top: 45px;
    background: var(--card-light);
    border-right: 1px solid var(--orange);
    border-bottom: 1px solid var(--orange);
  }
  .brand-mark {
    position: absolute;
    left: 0; right: 0; top: 130px;
    text-align: center;
    font-weight: 600;
    font-size: 210px;
    line-height: 1;
    letter-spacing: 6px;
    color: var(--orange);
  }
  .front-tagline {
    position: absolute;
    left: 0; right: 0; top: 410px;
    text-align: center;
    font-weight: 400;
    font-size: 40px;
    letter-spacing: 13px;
    padding-left: 13px;
    color: var(--ink);
  }

  /* Back */
  .card--back {
    top: 620px;
    background: var(--orange);
    overflow: hidden;
  }
  .back-sweep {
    position: absolute; inset: 0;
  }
  .back-title {
    position: absolute;
    left: 63px; top: 70px;
    width: 414px;
    font-weight: 400;
    font-size: 38px;
    letter-spacing: 9px;
    color: var(--white);
    padding-left: 2px;
    padding-bottom: 6px;
    border-bottom: 1px solid var(--white);
  }
  .contact {
    position: absolute;
    left: 77px;
    font-size: 20px;
    color: var(--white);
    text-transform: uppercase;
  }
  .contact--address { top: 190px; }
  .contact--map { top: 296px; }
  .social {
    position: absolute;
    left: 63px; top: 478px;
    display: flex; gap: 18px;
    list-style: none;
  }
  .social__item {
    display: flex; align-items: center; gap: 6px;
    font-size: 14px;
    color: var(--white);
  }
  .social__item::before {
    content: "";
    width: 16px; height: 16px;
    background: var(--white);
    border-radius: 3px;
  }
  .bean-pattern {
    position: absolute;
    left: 588px; top: 10px;
    width: 212px; height: 525px;
    border-radius: 40px;
    background: linear-gradient(180deg, rgba(165,71,28,0.85), rgba(165,71,28,0.75));
  }
</style>
</head>
<body>
  <section class="card card--front">
    <div class="brand-mark">RM</div>
    <p class="front-tagline">COFFEE HOUSE</p>
  </section>

  <section class="card card--back">
    <svg class="back-sweep" viewBox="0 0 826 545" preserveAspectRatio="none" aria-hidden="true">
      <path d="M0 545 C 220 260, 470 70, 826 0 L 826 545 Z" fill="var(--orange-soft)"/>
    </svg>
    <h1 class="back-title">COFFEE HOUSE</h1>
    <p class="contact contact--address">Steet Address: Coffee House</p>
    <p class="contact contact--map">Location Map: Coffee House</p>
    <ul class="social">
      <li class="social__item">Linkbook</li>
      <li class="social__item">PostPress</li>
      <li class="social__item">Pictogram</li>
    </ul>
    <div class="bean-pattern" role="img" aria-label="Column pattern of brown coffee beans"></div>
  </section>
</body>
</html>
```